Event flyer for Sunday night Youth Group

Need a 4 x 6 or 5 x 7 flyer for a new youth group starting on April 14. The youth group is for students in middle school and high school so it needs to look fun and cool, but not childish. I prefer it not to include pictures of people unless it's so obscure you can't really see their faces. I've uploaded some pictures of flyers I like. I've also attached a couple versions of our logo to use on the flyer.
Information the flyer needs to include:
Youth Group
Sundays, 6-8pm (beginning April 14)
Location: Merriwick's - 4219 Hollowfern Ln S, Keizer, 97418
There will be dinner, games, friends, and a message.
Target Market(s)
Youth ages 13-18
Industry/Entity Type
Church
Colors
Designer to choose colors to be used in the design.
Look and feel

```html
<!DOCTYPE html>
<html lang="en">
<head>
<meta charset="utf-8">
<title>Sundays Youth Group – Wayside Fellowship</title>
<link href="https://fonts.googleapis.com/css2?family=Montserrat:wght@500;700;900&family=Open+Sans:wght@400&family=Mrs+Saint+Delafield&display=swap" rel="stylesheet">
<style>
  :root {
    --night: #1b1033;
    --violet: #3a1f6e;
    --plum: #5b2d7f;
    --haze: #8a6ab8;
    --teal: #4fc6d3;
    --sky: #1fa3e0;
    --icon: #2aa6e6;
    --white: #ffffff;
    --ink: #0a0612;
  }
  * { margin: 0; padding: 0; box-sizing: border-box; }
  html, body { width: 800px; height: 1200px; overflow: hidden; background: var(--night); }
  .flyer {
    position: relative; width: 800px; height: 1200px; overflow: hidden;
    font-family: "Montserrat", sans-serif; color: var(--white);
  }
  .stage-backdrop {
    position: absolute; inset: 0;
    background:
      radial-gradient(ellipse 60% 30% at 50% 0%, rgba(90,150,255,.35), transparent 70%),
      radial-gradient(ellipse 50% 40% at 10% 25%, rgba(200,80,220,.30), transparent 70%),
      radial-gradient(ellipse 50% 40% at 90% 25%, rgba(80,120,255,.30), transparent 70%),
      linear-gradient(180deg, #2a1850 0%, #3b2070 45%, #2a1458 75%, #1a0c38 100%);
  }
  .crowd-band {
    position: absolute; left: 0; right: 0; bottom: 0; height: 290px;
    background: linear-gradient(180deg, transparent 0%, rgba(60,25,90,.7) 40%, rgba(70,20,60,.9) 100%);
  }
  .feature-panel {
    position: absolute; left: 130px; top: 253px; width: 540px; height: 574px;
    background: radial-gradient(ellipse 55% 60% at 50% 45%, #a793c9 0%, #6d4f9c 45%, rgba(60,35,110,.4) 100%);
    opacity: .85;
  }
  .brand { position: absolute; top: 40px; left: 0; width: 800px; text-align: center; }
  .brand-mark { width: 44px; height: 44px; background: var(--white); margin: 28px auto 34px; }
  .brand-name { font-weight: 500; font-size: 32px; letter-spacing: 1px; line-height: 1; }
  .brand-sub { font-weight: 500; font-size: 16px; letter-spacing: 6px; margin-top: 10px; line-height: 1; }
  .title-script {
    position: absolute; top: 250px; left: 0; width: 800px; text-align: center;
    font-family: "Mrs Saint Delafield", cursive; font-size: 200px; line-height: 1;
    color: var(--teal); z-index: 3; transform: rotate(-4deg);
  }
  .title-main {
    position: absolute; top: 430px; left: 0; width: 800px; text-align: center;
    font-weight: 900; font-size: 128px; line-height: 1; letter-spacing: -3px;
    text-shadow: 6px 4px 0 var(--ink); transform: scaleX(1.18); z-index: 2;
  }
  .title-sub {
    position: absolute; top: 556px; left: 0; width: 800px; text-align: center;
    font-weight: 900; font-size: 60px; line-height: 1; letter-spacing: -1px; z-index: 2;
  }
  .date {
    position: absolute; top: 722px; left: 0; width: 800px; text-align: center;
    font-weight: 700; font-size: 64px; line-height: 1; letter-spacing: -1px;
  }
  .schedule {
    position: absolute; top: 793px; left: 247px; width: 306px; height: 52px;
    background: var(--sky); text-align: center;
    font-weight: 700; font-size: 31px; line-height: 52px;
  }
  .venue {
    position: absolute; top: 878px; left: 0; width: 800px; text-align: center;
    font-weight: 500; font-size: 26px; line-height: 33px;
  }
  .features { position: absolute; top: 980px; left: 0; width: 800px; height: 110px; }
  .feature-icon { position: absolute; top: 20px; width: 80px; height: 80px; }
  .divider { position: absolute; top: 0; width: 8px; height: 110px; }
  .tagline {
    position: absolute; top: 1118px; left: 0; width: 800px; text-align: center;
    font-family: "Open Sans", sans-serif; font-size: 24px;
  }
</style>
</head>
<body>
<div class="flyer">
  <div class="stage-backdrop" role="img" aria-label="Concert stage with colourful light beams"></div>
  <div class="crowd-band" role="img" aria-label="Silhouetted crowd in the dark"></div>
  <div class="feature-panel" role="img" aria-label="Church interior with a large cross in purple light"></div>

  <header class="brand">
    <div class="brand-mark"></div>
    <div class="brand-name">WAYSIDE</div>
    <div class="brand-sub">FELLOWSHIP</div>
  </header>

  <h1>
    <span class="title-script">Sundays</span>
    <span class="title-main">YOUTH</span>
    <span class="title-sub">GROUP</span>
  </h1>

  <p class="date">APRIL 14</p>
  <p class="schedule">SUNDAYS, 6-8PM</p>
  <p class="venue">Merriwick's - 4219 Hollowfern Ln S,<br>Keizer, 97418</p>

  <div class="features">
    <svg class="feature-icon" style="left:167px" viewBox="0 0 80 80" fill="none" stroke="var(--icon)" stroke-width="3" aria-label="Dinner">
      <circle cx="40" cy="40" r="36"/><circle cx="40" cy="40" r="26"/>
      <path d="M30 22v14a4 4 0 0 0 8 0V22M34 22v36M50 22c-5 4-5 16 0 20v16"/>
    </svg>
    <svg class="divider" style="left:261px" viewBox="0 0 8 110" stroke="var(--white)" stroke-width="1.5" aria-hidden="true"><path d="M4 0v110M0 1h8M0 109h8"/></svg>
    <svg class="feature-icon" style="left:295px" viewBox="0 0 80 80" fill="none" stroke="var(--icon)" stroke-width="3" aria-label="Games">
      <path d="M20 24h40c8 0 12 8 14 20s2 20-6 20c-6 0-8-10-14-10H26c-6 0-8 10-14 10-8 0-8-8-6-20s6-20 14-20z"/>
      <path d="M22 34v12M16 40h12"/><circle cx="54" cy="35" r="2.5"/><circle cx="60" cy="41" r="2.5"/><circle cx="54" cy="47" r="2.5"/><circle cx="48" cy="41" r="2.5"/>
      <path d="M34 42h4M42 42h4"/>
    </svg>
    <svg class="divider" style="left:398px" viewBox="0 0 8 110" stroke="var(--white)" stroke-width="1.5" aria-hidden="true"><path d="M4 0v110M0 1h8M0 109h8"/></svg>
    <div class="feature-icon" style="left:429px; border:3px solid var(--icon); border-radius:10px; width:70px; height:70px; top:25px" role="img" aria-label="Friends high-five icon"></div>
    <svg class="divider" style="left:531px" viewBox="0 0 8 110" stroke="var(--white)" stroke-width="1.5" aria-hidden="true"><path d="M4 0v110M0 1h8M0 109h8"/></svg>
    <svg class="feature-icon" style="left:553px" viewBox="0 0 80 80" fill="none" stroke="var(--icon)" stroke-width="3" aria-label="Message">
      <path d="M24 10h50v34h-8v8l-8-8"/>
      <path d="M6 22h52v36H24l-12 12V58H6z"/>
      <path d="M14 34h34M14 42h34M14 50h22"/>
    </svg>
  </div>

  <p class="tagline">There will be dinner, games, friends, and a message.</p>
</div>
</body>
</html>
```